Pegan Pyramid

Need a graphic for community lecture next week on preventing Cognitive Decline. Would like a Food Pyramid very similar to the one at this link, but with some adjustments:
1. Picture of "non-startchy veggie plant foods" might also include purple onion, garlic, purple cabbage, shitake mushrooms (in addition to what's pictured)
2. "Protein & Healthy Fats" would say "Mindful Protein & Healthy Fats". Picture should also include olive oil
3. Picture of starchy veggies would be more carrot/yam/beets/squash
http://www.tovashlend.com/wellness/grain-free-greens-the-plan-nobody-told-you-about/
Look forward to your design!!

```html
<!DOCTYPE html>
<html lang="en">
<head>
<meta charset="utf-8">
<title>Pegan Pyramid</title>
<link rel="stylesheet" href="https://fonts.googleapis.com/css2?family=Signika:wght@600&display=swap">
<style>
  :root {
    --bg: #ffffff;
    --ink: #ffffff;
    --purple: #a24fb4;
    --purple-light: #c07fcb;
    --purple-dark: #7d3590;
    --teal: #22c8a8;
    --teal-light: #45e2c6;
    --teal-dark: #12957c;
    --pink: #e6268a;
    --pink-light: #ef78ae;
    --pink-dark: #b81468;
    --blue: #1e87d8;
    --blue-light: #8ed2f2;
    --blue-dark: #1763b0;
    --orange: #ef8a22;
    --orange-light: #f7b04d;
    --orange-dark: #d06b10;
    --green: #3cb54a;
    --green-light: #8ad32e;
    --green-dark: #0d9a4a;
    --silver: #d9d9d9;
  }
  html, body {
    margin: 0;
    padding: 0;
    width: 1200px;
    height: 1200px;
    overflow: hidden;
    background: var(--bg);
  }
  .pyramid {
    display: block;
    width: 1200px;
    height: 1200px;
  }
  .tier-label, .tier-rule {
    font-family: "Signika", "Trebuchet MS", sans-serif;
    font-weight: 600;
    fill: var(--ink);
    text-anchor: middle;
    text-transform: uppercase;
  }
  .tier-rule { font-size: 22px; letter-spacing: 0.5px; }
  .fold { opacity: 0.95; }
  .divider { fill: var(--silver); }
</style>
</head>
<body>
<svg class="pyramid" viewBox="0 0 1200 1200" xmlns="http://www.w3.org/2000/svg">
  <defs>
    <linearGradient id="band-purple" x1="0" x2="1"><stop offset="0" stop-color="var(--purple)"/><stop offset="1" stop-color="var(--purple-light)"/></linearGradient>
    <linearGradient id="band-teal" x1="0" x2="1"><stop offset="0" stop-color="var(--teal)"/><stop offset="0.5" stop-color="var(--teal-light)"/><stop offset="1" stop-color="var(--teal)"/></linearGradient>
    <linearGradient id="band-pink" x1="0" x2="1"><stop offset="0" stop-color="var(--pink)"/><stop offset="1" stop-color="var(--pink-light)"/></linearGradient>
    <linearGradient id="band-blue" x1="0" x2="1"><stop offset="0" stop-color="var(--blue-dark)"/><stop offset="1" stop-color="var(--blue-light)"/></linearGradient>
    <linearGradient id="band-orange" x1="0" x2="1"><stop offset="0" stop-color="var(--orange)"/><stop offset="1" stop-color="var(--orange-light)"/></linearGradient>
    <linearGradient id="band-green" x1="0" x2="1"><stop offset="0" stop-color="var(--green-light)"/><stop offset="0.5" stop-color="var(--green)"/><stop offset="1" stop-color="var(--green-dark)"/></linearGradient>
    <linearGradient id="photo-treats" x1="0" y1="0" x2="0" y2="1"><stop offset="0" stop-color="#5a2a22"/><stop offset="1" stop-color="#c9b3a8"/></linearGradient>
    <linearGradient id="photo-spices" x1="0" x2="1"><stop offset="0" stop-color="#b8461f"/><stop offset="0.5" stop-color="#d9a23a"/><stop offset="1" stop-color="#6b4a2e"/></linearGradient>
    <linearGradient id="photo-beans" x1="0" x2="1"><stop offset="0" stop-color="#b9a07a"/><stop offset="0.5" stop-color="#8a2a25"/><stop offset="1" stop-color="#d8b84a"/></linearGradient>
    <linearGradient id="photo-fruits" x1="0" x2="1"><stop offset="0" stop-color="#c4232f"/><stop offset="0.6" stop-color="#3f4f8f"/><stop offset="1" stop-color="#b0243a"/></linearGradient>
    <linearGradient id="photo-starchy" x1="0" x2="1"><stop offset="0" stop-color="#c8552a"/><stop offset="0.5" stop-color="#ee8a3a"/><stop offset="1" stop-color="#7a3a44"/></linearGradient>
    <linearGradient id="photo-protein" x1="0" x2="1"><stop offset="0" stop-color="#a82e2e"/><stop offset="0.5" stop-color="#e3c27a"/><stop offset="1" stop-color="#e7b3a8"/></linearGradient>
    <linearGradient id="photo-veggies" x1="0" x2="1"><stop offset="0" stop-color="#7a3f7f"/><stop offset="0.5" stop-color="#5e9a3c"/><stop offset="1" stop-color="#e9e4d6"/></linearGradient>
  </defs>

  <!-- Tier: recreational treats -->
  <g class="tier tier-treats">
    <polygon class="fold" fill="var(--purple-dark)" points="470,97 495,80 560,243 540,260"/>
    <polygon fill="url(#band-purple)" points="495,80 1200,80 1200,243 560,243"/>
    <polygon role="img" aria-label="Photo of chocolate cake, desserts and wine bottles" fill="url(#photo-treats)" points="470,97 505,97 535,222 415,222"/>
    <polygon fill="var(--purple)" points="415,222 538,222 545,258 399,258"/>
    <text class="tier-label" font-size="13" x="473" y="237">Recreational</text>
    <text class="tier-label" font-size="13" x="473" y="253">Treats</text>
    <text class="tier-rule" font-size="24" x="877" y="174">Sparingly</text>
  </g>

  <!-- Tier: spices and herbs -->
  <g class="tier tier-spices">
    <polygon role="img" aria-label="Photo of bowls of colourful spices and herbs" fill="url(#photo-spices)" points="394,268 440,268 492,413 330,413"/>
    <polygon class="divider" points="440,268 458,268 510,413 492,413"/>
    <polygon fill="var(--teal)" points="458,268 552,268 602,413 510,413"/>
    <polygon class="fold" fill="var(--teal-dark)" points="552,268 570,268 620,403 602,413"/>
    <polygon fill="url(#band-teal)" points="570,268 1200,268 1200,403 620,403"/>
    <text class="tier-label" font-size="18" x="528" y="329">Spices</text>
    <text class="tier-label" font-size="18" x="528" y="354">and</text>
    <text class="tier-label" font-size="18" x="528" y="378">Herbs</text>
    <text class="tier-rule" x="885" y="328">Unlimited</text>
    <text class="tier-rule" x="885" y="356">Amounts</text>
  </g>

  <!-- Tier: beans, legumes, grains -->
  <g class="tier tier-beans">
    <polygon role="img" aria-label="Photo of assorted beans, lentils and grains" fill="url(#photo-beans)" points="327,432 400,432 450,577 260,577"/>
    <polygon class="divider" points="400,432 418,432 468,577 450,577"/>
    <polygon fill="var(--pink-light)" points="418,432 620,432 680,577 468,577"/>
    <polygon class="fold" fill="var(--pink-dark)" points="620,432 640,420 690,565 680,577"/>
    <polygon fill="url(#band-pink)" points="640,420 1200,420 1200,565 690,565"/>
    <text class="tier-label" font-size="15" x="550" y="501">Beans, Legumes,</text>
    <text class="tier-label" font-size="15" x="550" y="522">Non Gluten Grains</text>
    <text class="tier-rule" x="925" y="472">Include up to 1/2</text>
    <text class="tier-rule" x="925" y="501">cup of gluten free grains, up to 1/2</text>
    <text class="tier-rule" x="925" y="529">cup-1cup of beans</text>
  </g>

  <!-- Tier: fruits and starchy veggies -->
  <g class="tier tier-fruits">
    <polygon role="img" aria-label="Photo of strawberries, raspberries and blueberries" fill="url(#photo-fruits)" points="250,598 440,598 470,695 212,695"/>
    <polygon role="img" aria-label="Photo of carrots, yams, beets and squash" fill="url(#photo-starchy)" points="448,598 700,598 700,695 478,695"/>
    <polygon fill="url(#band-blue)" points="212,695 470,695 486,742 186,742"/>
    <polygon class="divider" points="470,695 486,695 502,742 486,742"/>
    <polygon fill="var(--blue-dark)" points="486,695 750,695 750,742 502,742"/>
    <polygon class="fold" fill="var(--blue)" points="695,598 712,585 772,730 750,742"/>
    <polygon fill="url(#band-blue)" points="712,585 1200,585 1200,730 772,730"/>
    <text class="tier-label" font-size="28" x="338" y="728">Fruits</text>
    <text class="tier-label" font-size="21" x="620" y="726">Starchy Veggies</text>
    <text class="tier-rule" x="990" y="636">Focus on low glycemic fruit</text>
    <text class="tier-rule" x="990" y="664">(1 cup per day) &amp; up to 2 servings</text>
    <text class="tier-rule" x="990" y="692">of starchy veggies per day</text>
  </g>

  <!-- Tier: protein and fats -->
  <g class="tier tier-protein">
    <polygon role="img" aria-label="Photo of meat, fish, eggs, cheese, bread, pasta and olive oil" fill="url(#photo-protein)" points="180,762 390,762 440,907 113,907"/>
    <polygon class="divider" points="390,762 408,762 458,907 440,907"/>
    <polygon fill="var(--orange)" points="408,762 770,762 820,907 458,907"/>
    <polygon class="fold" fill="var(--orange-dark)" points="770,762 790,750 840,890 820,907"/>
    <polygon fill="url(#band-orange)" points="790,750 1200,750 1200,890 840,890"/>
    <text class="tier-label" font-size="28" x="615" y="827">Mindful Protein &amp;</text>
    <text class="tier-label" font-size="28" x="615" y="861">Healthy Fats</text>
    <text class="tier-rule" x="1005" y="799">4-6 oz of protein</text>
    <text class="tier-rule" x="1005" y="828">per meal, &amp; 3-5 servings</text>
    <text class="tier-rule" x="1005" y="857">of fat per day</text>
  </g>

  <!-- Tier: non starchy veggies -->
  <g class="tier tier-veggies">
    <polygon role="img" aria-label="Photo of cabbages, cauliflower, purple onion, garlic, broccoli and shiitake mushrooms" fill="url(#photo-veggies)" points="109,925 345,925 400,1078 35,1078"/>
    <polygon class="divider" points="345,925 365,925 420,1078 400,1078"/>
    <polygon fill="var(--green)" points="365,925 840,925 905,1078 420,1078"/>
    <polygon class="fold" fill="var(--green-light)" points="840,925 855,912 915,1062 905,1078"/>
    <polygon fill="var(--green-dark)" points="855,912 1200,912 1200,1062 915,1062"/>
    <text class="tier-label" font-size="30" x="623" y="993">Non Starchy Veggie</text>
    <text class="tier-label" font-size="30" x="623" y="1032">Plant Foods</text>
    <text class="tier-rule" font-size="21" x="1027" y="981">Unlimited</text>
    <text class="tier-rule" font-size="21" x="1027" y="1009">Amounts</text>
  </g>
</svg>
</body>
</html>
```